Geothermal company needs a creative "POW" business card

Manufacturers tend to be boring. We are not! We are a Geothermal Heat Pump company that has over 30 yrs of experience and wants a new look and updated feel. Nothing old (yawn) so get your creative hats on and let's rock!

We want to use the great colors of lime green and navy blue. Our new logo is attached and we're ready to roll. Remember, we're a professional leader in the geothermal industry that needs to make an eye catching and memorable first glance.

```html
<!DOCTYPE html>
<html lang="en">
<head>
<meta charset="utf-8">
<title>Boreal Terra – Business Card</title>
<link rel="stylesheet" href="https://fonts.googleapis.com/css2?family=Open+Sans:wght@400;600;700&family=PT+Sans+Narrow:wght@400;700&display=swap">
<style>
  :root {
    --bg: #2b1c14;
    --navy: #1b3f7e;
    --lime: #7cc520;
    --leaf-green: #3f9a1e;
    --deep-blue: #155b9f;
    --teal: #1f8f8c;
    --aqua: #46c9b4;
    --white: #ffffff;
    --ink: #22457f;
  }
  * { box-sizing: border-box; margin: 0; padding: 0; }
  html, body { width: 1200px; height: 1000px; overflow: hidden; }
  body {
    background: var(--bg);
    font-family: "Open Sans", Arial, sans-serif;
    display: flex;
    flex-direction: column;
    align-items: center;
    justify-content: center;
    gap: 44px;
  }
  .card {
    position: relative;
    width: 760px;
    height: 434px;
    overflow: hidden;
    box-shadow: 0 10px 30px rgba(0,0,0,.55);
  }
  .card__sky {
    position: absolute; inset: 0;
    background:
      radial-gradient(ellipse 70% 22% at 60% 14%, rgba(120,235,210,.55), transparent 70%),
      radial-gradient(ellipse 60% 30% at 25% 80%, rgba(60,150,220,.45), transparent 70%),
      linear-gradient(170deg, var(--teal) 0%, var(--deep-blue) 48%, var(--teal) 72%, var(--deep-blue) 100%);
  }
  .card--back .card__sky {
    background:
      radial-gradient(ellipse 70% 20% at 55% 22%, rgba(130,240,200,.6), transparent 70%),
      radial-gradient(ellipse 50% 25% at 80% 78%, rgba(90,210,190,.4), transparent 70%),
      linear-gradient(170deg, #2a8b7a 0%, var(--teal) 35%, var(--deep-blue) 75%, #1b6aa6 100%);
  }
  .card__band {
    position: absolute;
    left: 0; right: 0;
    background: var(--white);
    display: flex;
    align-items: center;
  }
  .card--front .card__band { top: 136px; height: 132px; padding-left: 46px; gap: 22px; }
  .card--back .card__band { top: 152px; height: 124px; padding-left: 44px; }

  .brand-dot {
    width: 88px; height: 88px; border-radius: 50%;
    background: var(--deep-blue);
    flex: none;
  }
  .brand__name {
    font-weight: 700;
    font-size: 60px;
    line-height: 1;
    color: var(--lime);
    letter-spacing: -0.5px;
  }
  .brand__tagline {
    font-family: "PT Sans Narrow", "Arial Narrow", sans-serif;
    font-weight: 700;
    font-size: 19px;
    color: var(--navy);
    margin-top: 6px;
  }

  .person { display: flex; align-items: center; gap: 14px; width: 300px; }
  .person-dot { width: 40px; height: 40px; border-radius: 50%; background: var(--leaf-green); flex: none; }
  .person__name { font-size: 22px; color: var(--ink); line-height: 1.1; }
  .person__role { font-size: 15px; color: var(--leaf-green); letter-spacing: .3px; }

  .contact { list-style: none; font-size: 17px; color: var(--ink); line-height: 1.25; }
  .contact__label { display: inline-block; width: 20px; font-size: 14px; color: var(--leaf-green); }
</style>
</head>
<body>
  <section class="card card--front" aria-label="Business card front">
    <div class="card__sky" role="img" aria-label="Soft teal and blue aurora-like gradient"></div>
    <div class="card__band">
      <span class="brand-dot"></span>
      <div class="brand">
        <div class="brand__name">Boreal Terra</div>
        <div class="brand__tagline">Manufacturer of Geothermal Heat Pumps for the North</div>
      </div>
    </div>
  </section>

  <section class="card card--back" aria-label="Business card back">
    <div class="card__sky" role="img" aria-label="Soft teal and blue aurora-like gradient"></div>
    <div class="card__band">
      <div class="person">
        <span class="person-dot"></span>
        <div>
          <div class="person__name">Alex Marlow</div>
          <div class="person__role">GENERAL MANAGER</div>
        </div>
      </div>
      <ul class="contact">
        <li><span class="contact__label">p</span>555 010 2040</li>
        <li><span class="contact__label">f</span>555 010 2040</li>
        <li><span class="contact__label">e</span>alexmarlow@borealterra.com</li>
        <li><span class="contact__label">w</span>www.borealterra.com</li>
      </ul>
    </div>
  </section>
</body>
</html>
```